*Must be in spanish

Web Site In spanish for velmtra.com

A brand awareness web site. The domain currently has an JPG. The only thing that works right now is the email link. The JPG doesn´t really appeal the target we´re trying to reach. We Only need for our customers to be able to contact us and get the correct impression of our services.

In the products page we need to show all the tires we can make, they are 40 different kinds of tires.

Target Market(s)

Buyers in logistic department, bus companies, and trucks owners.

Requirements
Must have
• All the info is in the .doc
Nice to have
• Facebook share, twitter twit this and +1 also there is more info In the .doc

```html
<!DOCTYPE html>
<html lang="es">
<head>
<meta charset="utf-8">
<title>Velmtra · Neumáticos</title>
<link rel="stylesheet" href="https://fonts.googleapis.com/css2?family=Crimson+Text:ital,wght@0,400;0,600;1,400&family=Roboto+Condensed:wght@300;400&display=swap">
<style>
:root{
  --page:#e6e6e6;
  --header:#e9e9e9;
  --blue:#23389e;
  --ink-blue:#1f3f7a;
  --hero-bg:#050b1e;
  --text:#5a5a5a;
  --rule:#c9c9c9;
  --card:#f2f2f2;
  --footer:#1c1c1c;
  --footer-base:#141414;
  --footer-text:#6a6a6a;
  --footer-head:#d6d6d6;
  --link:#3a7cc0;
}
*{margin:0;padding:0;box-sizing:border-box}
html,body{width:934px;height:1200px;overflow:hidden}
body{position:relative;background:var(--page);font-family:"Roboto Condensed","Arial Narrow",sans-serif;font-weight:300;color:var(--text)}
.abs{position:absolute}
.site-header{left:0;top:0;width:934px;height:60px;background:linear-gradient(#f0f0f0,var(--header));border-top:6px solid #fff}
.nav a{position:absolute;top:20px;font:italic 13px "Crimson Text",serif;color:#666;text-decoration:none;white-space:nowrap}
.nav a.active{color:var(--blue)}
.brand-tab{left:382px;top:0;width:170px;height:62px;background:linear-gradient(#fafafa,#e2e2e2);border-left:2px solid #bbb;border-right:2px solid #bbb;display:flex;align-items:center;justify-content:center}
.brand-name{font:600 28px "Crimson Text",serif;color:var(--blue);letter-spacing:1px}
.blue-band{left:0;top:60px;width:934px;height:12px;background:var(--blue)}
.hero{left:0;top:72px;width:934px;height:227px;background:var(--hero-bg)}
.hero-photo{left:130px;top:72px;width:670px;height:227px;background:linear-gradient(160deg,#8fb56a 0%,#6f8f4a 35%,#9aa3a8 60%,#4a5560 100%)}
.hero-edge{left:0;top:299px;width:934px;height:7px;background:#fafafa}
.section-title{left:0;top:322px;width:934px;text-align:center;font:400 13px "Crimson Text",serif;letter-spacing:1px;color:#555}
.title-rule{top:333px;height:1px;background:var(--rule);border-bottom:1px solid #fff}
.product{width:220px;text-align:center}
.product-img{margin:0 auto;width:84px;height:84px;border-radius:50%;background:radial-gradient(circle,#f4f4f4 15%,#9a9a9a 45%,#3a3a3a 75%)}
.product-img.tyre{width:110px;border-radius:40px;background:radial-gradient(circle,#d8d8d8 15%,#777 40%,#1e1e1e 65%)}
.product-shadow{margin:6px auto 0;width:70px;height:6px;border-radius:50%;background:radial-gradient(#aaa,transparent 70%)}
.product h3{margin-top:23px;font:400 13px "Crimson Text",serif;letter-spacing:.5px;color:#555}
.product p{margin-top:9px;font-size:9px;line-height:16px;letter-spacing:.3px;color:#666;white-space:nowrap}
.read-more{display:inline-block;margin-top:6px;font-size:8.5px;font-weight:400;letter-spacing:.4px;color:var(--ink-blue);text-decoration:none}
.arrow{display:inline-block;width:0;height:0;border-left:3px solid currentColor;border-top:3px solid transparent;border-bottom:3px solid transparent;margin-left:4px;vertical-align:middle}
.feature-card{left:133px;top:617px;width:668px;height:311px;background:var(--card);border:1px solid #d8d8d8}
.feature{top:13px;width:304px}
.feature h2{font:300 17px "Roboto Condensed",sans-serif;letter-spacing:.6px;color:#333;height:38px;border-bottom:1px solid #bbb}
.feature p{margin-top:9px;height:64px;font-size:8.5px;line-height:16px;letter-spacing:.2px;color:#555}
.feature-photo{position:absolute;top:119px;left:0;width:304px;height:111px;background:linear-gradient(120deg,#6fb4b8 0%,#9fd3d2 45%,#3d7078 80%,#2a3d48 100%)}
.learn-more{left:0;top:272px;width:666px;text-align:center;font:400 11px "Crimson Text",serif;letter-spacing:1.2px;color:var(--ink-blue);text-decoration:none}
.site-footer{left:0;top:950px;width:934px;height:238px;background:var(--footer)}
.footer-base{left:0;top:1188px;width:934px;height:12px;background:var(--footer-base)}
.footer-col{top:26px;width:199px}
.footer-col h4{font:400 11px "Crimson Text",serif;letter-spacing:1.2px;color:var(--footer-head);padding-bottom:8px;border-bottom:1px solid #444}
.news-item{display:flex;gap:13px;margin-top:14px;height:38px}
.news-thumb{width:38px;height:38px;flex:none;background:linear-gradient(135deg,#1b3a8a,#6b8fc0 50%,#0d1a40)}
.news-thumb.road{background:linear-gradient(135deg,#6e9a4a,#aab4a0 50%,#2a3440)}
.news-body{flex:1;border-bottom:1px solid #333;padding-top:4px}
.news-body strong{display:block;font-weight:300;font-size:9px;letter-spacing:.6px;color:#ccc;margin-bottom:2px}
.news-body span{font-size:8px;letter-spacing:.4px;color:var(--footer-text)}
.footer-text{margin-top:10px;font-size:8px;line-height:16px;letter-spacing:.4px;color:var(--footer-text)}
.footer-text a{color:var(--link);text-decoration:none}
.footer-list{list-style:none;margin-top:12px}
.footer-list li{font-size:8px;letter-spacing:.4px;color:var(--footer-text);margin-bottom:15px;padding-left:12px;position:relative;white-space:nowrap}
.footer-list li::before{content:"";position:absolute;left:0;top:3px;border-left:3px solid var(--link);border-top:3px solid transparent;border-bottom:3px solid transparent}
.social{display:flex;gap:18px;margin-top:16px}
.social span{width:24px;height:24px;border-radius:50%;background:radial-gradient(circle at 40% 35%,#555,#2a2a2a);box-shadow:0 1px 2px #000}
.social span.on{background:radial-gradient(circle at 40% 35%,#bfe3f3,#5aa9cc)}
</style>
</head>
<body>
<header class="abs site-header">
  <nav class="nav">
    <a class="active" style="left:134px" href="#">Inicio</a>
    <a style="left:206px" href="#">Empresa</a>
    <a style="left:286px" href="#">Productos</a>
    <a style="left:589px" href="#">Servicios</a>
    <a style="left:693px" href="#">Noticias</a>
    <a style="left:762px" href="#">Contacto</a>
  </nav>
</header>
<div class="abs brand-tab"><span class="brand-name">VELMTRA</span></div>
<div class="abs blue-band"></div>
<div class="abs hero"></div>
<div class="abs hero-photo" role="img" aria-label="Automóvil circulando rápido por una carretera de montaña con árboles"></div>
<div class="abs hero-edge"></div>

<div class="abs title-rule" style="left:134px;width:250px"></div>
<div class="abs title-rule" style="left:550px;width:250px"></div>
<h2 class="abs section-title">NUESTROS PRODUCTOS</h2>

<div class="abs product" style="left:115px;top:356px">
  <div class="product-img" role="img" aria-label="Rin de aleación"></div>
  <div class="product-shadow"></div>
  <h3>Nombre del producto</h3>
  <p>Neumáticos diseñados para largas rutas de<br>carga, con gran resistencia al desgaste y<br>excelente agarre en carreteras mojadas y<br>secas para flotas de reparto y logística.</p>
  <a class="read-more" href="#">LEER MÁS<i class="arrow"></i></a>
</div>
<div class="abs product" style="left:357px;top:356px">
  <div class="product-img tyre" role="img" aria-label="Dos neumáticos apilados con rines"></div>
  <div class="product-shadow"></div>
  <h3>Nombre del producto</h3>
  <p>Neumáticos para autobuses urbanos y de<br>pasajeros, pensados para soportar miles de<br>paradas diarias con un rodaje suave, seguro<br>y un consumo de combustible reducido.</p>
  <a class="read-more" href="#">LEER MÁS<i class="arrow"></i></a>
</div>
<div class="abs product" style="left:594px;top:356px">
  <div class="product-img" role="img" aria-label="Rin plateado de radios múltiples"></div>
  <div class="product-shadow"></div>
  <h3>Nombre del producto</h3>
  <p>Neumáticos para camiones de carga pesada,<br>con estructura reforzada y banda de rodadura<br>profunda para trabajar en obra, minería y<br>caminos difíciles durante todo el año.</p>
  <a class="read-more" href="#">LEER MÁS<i class="arrow"></i></a>
</div>

<section class="abs feature-card">
  <article class="abs feature" style="left:19px">
    <h2>Soluciones para su flotilla</h2>
    <p>Fabricamos neumáticos para departamentos de logística, empresas de autobuses y propietarios de camiones. Cada modelo se prueba para ofrecer más kilómetros, mayor seguridad y menos paradas en taller. Contamos con cuarenta tipos de neumáticos distintos para cada necesidad de su operación diaria.</p>
    <div class="feature-photo" role="img" aria-label="Lateral trasero de un automóvil deportivo turquesa"></div>
  </article>
  <article class="abs feature" style="left:353px">
    <h2>Calidad que se nota en el camino</h2>
    <p>Nuestro equipo le asesora para elegir el neumático adecuado según la carga, la ruta y el clima. Ofrecemos atención directa, entregas puntuales y seguimiento después de la venta. Escríbanos y uno de nuestros asesores se pondrá en contacto con usted a la brevedad posible.</p>
    <div class="feature-photo" role="img" aria-label="Lateral trasero de un automóvil deportivo turquesa"></div>
  </article>
  <a class="abs learn-more" href="#">CONOZCA MÁS<i class="arrow"></i></a>
</section>

<footer class="abs site-footer">
  <div class="abs footer-col" style="left:134px">
    <h4>ÚLTIMAS NOTICIAS</h4>
    <div class="news-item"><div class="news-thumb" role="img" aria-label="Rueda de automóvil azul"></div><div class="news-body"><strong>NUEVA LÍNEA DE CARGA</strong><span>Presentamos modelos para rutas largas</span></div></div>
    <div class="news-item"><div class="news-thumb road" role="img" aria-label="Automóvil en carretera"></div><div class="news-body"><strong>FLOTAS DE AUTOBÚS</strong><span>Más kilómetros por cada neumático</span></div></div>
    <div class="news-item"><div class="news-thumb" role="img" aria-label="Rueda de automóvil azul"></div><div class="news-body"><strong>SERVICIO TÉCNICO</strong><span>Asesoría gratuita para su empresa</span></div></div>
  </div>
  <div class="abs footer-col" style="left:368px">
    <h4>CONOZCA MÁS</h4>
    <p class="footer-text">Somos fabricantes de neumáticos para transporte de carga y pasajeros. Trabajamos con empresas de logística, líneas de autobuses y transportistas independientes <a href="#">leer más</a></p>
    <ul class="footer-list">
      <li>Cuarenta tipos de neumáticos disponibles</li>
      <li>Asesoría para elegir el modelo adecuado</li>
      <li>Entregas puntuales en todo el país</li>
    </ul>
  </div>
  <div class="abs footer-col" style="left:602px">
    <h4>DATOS DE CONTACTO</h4>
    <p class="footer-text">Calle Ejemplo 123<br>Ciudad y/o colonia<br>Nombre del país<br>C.P. 00000<br>Teléfono : <a href="#">0800 555 0147</a><br>Correo : <a href="#">info@velmtra.com</a></p>
    <div class="social"><span aria-label="Red social"></span><span class="on" aria-label="Red social"></span><span aria-label="Red social"></span><span aria-label="Suscripción de noticias"></span></div>
  </div>
</footer>
<div class="abs footer-base"></div>
</body>
</html>
```